"MEET THE TEAM" page web design

We need a "meet the team" page for our website!
Please look at our website to see the style we need

We are looking for something unique, fun, cool, technology-style and yet professional. We plan on taking a picture of each employee (not sure if this will be a real photo/caricature/ black and white/goofy picture--> but we are open to any ideas you have that will work with the design) and putting it there, along with a little bio about each person.

Thanks! looking forward to working together:)
Updates

Project Deadline Extended
Reason: I am excited to see more designs and find the perfect fit. Thanks designers :)

Target Market(s)

People looking to purchase servers, workstations, components

Industry/Entity Type

Information Technology

Number of Pages Required

1 page

Font styles to use
Sans Serif
Other font styles liked:
• The font we use on our site so it matches

Requirements
Must have
• please look at our website qondimex.com and see the theme and colors we want.
• We have 13 employees but would like to have a design where we can add/remove people if we hire/terminate them without messing up the design.
• We are looking for something unique, fun, cool, technology-style and yet professional. We plan on taking a picture of each employee (not sure if this will be a real photo/caricature/ black and white/goofy picture--> but we are open to any ideas you have that will work with the design) and putting it there, along with a little bio about each person.
• We can upload anything you need
Nice to have
• We are also interested in having a design where when the cursor moves over a person then the bio comes out or moves around, or something. (This is not required, but we would love some cool ideas) And if you can come up with some design, we would have our programmers create it for us.
Should not have
• we are open to anything

```html
<!DOCTYPE html>
<html lang="en">
<head>
<meta charset="utf-8">
<title>Meet our team – Qondimex</title>
<link href="https://fonts.googleapis.com/css2?family=Arimo:wght@400;700&display=swap" rel="stylesheet">
<style>
:root{
  --teal:#4dbcb4;
  --teal-dark:#3aa79f;
  --ink:#333;
  --muted:#8a8a8a;
  --line:#dcdcdc;
  --footer:#a4a4a4;
  --footer-deep:#9b9b9b;
  --white:#fff;
}
*{box-sizing:border-box;margin:0;padding:0}
html,body{width:676px;height:1200px;overflow:hidden;background:var(--white)}
body{position:relative;font-family:"Arimo",Helvetica,Arial,sans-serif;color:var(--ink)}
.site-header{position:absolute;left:0;top:0;width:676px;height:41px;border-bottom:1px solid #e4e4e4}
.brand{position:absolute;left:84px;top:12px;display:flex;align-items:center;gap:6px}
.brand-dot{width:15px;height:15px;border-radius:50%;background:var(--teal)}
.brand-name{font-size:13px;font-weight:700;color:var(--teal);letter-spacing:.5px}
.main-nav{position:absolute;left:84px;top:47px;width:508px;height:15px;display:flex;align-items:center}
.main-nav a{font-size:6.4px;color:var(--ink);text-decoration:none;margin-right:11px}
.search{position:absolute;left:472px;top:47px;width:100px;height:15px;border:1px solid #ddd;border-radius:8px;font-size:5.5px;color:#777;padding:4px 8px}
.basket{position:absolute;left:575px;top:46px;width:16px;height:16px;border-radius:50%;background:var(--teal)}
.crumbs{position:absolute;left:0;top:67px;width:676px;height:20px;background:var(--teal);display:flex;align-items:center;padding-left:84px;font-size:6.4px;color:var(--white);gap:6px}
.intro{position:absolute;left:0;top:130px;width:676px;text-align:center}
.intro h1{font-weight:400;font-size:12.2px;line-height:14px;color:#444}
.intro p{margin:9px auto 0;width:264px;font-size:5.9px;line-height:7.2px;color:#999}
.team{position:absolute;left:84.5px;top:241px;width:507px;display:grid;grid-template-columns:repeat(4,1fr);gap:5.5px 5px}
.member{height:219px;border:1px solid var(--line);border-radius:3px;overflow:hidden;display:flex;flex-direction:column;background:var(--white)}
.member-photo{height:59px;flex:none}
.member-body{padding:7px 10px 0;flex:1}
.member-name{font-weight:400;font-size:11.4px;line-height:13px;color:#333}
.member-role{font-size:7.3px;color:#888;margin-top:1px}
.member-bio{font-size:5.4px;line-height:7.1px;color:#9a9a9a;margin-top:6px}
.member-bio+.member-bio{margin-top:6px}
.member-links{height:24px;border-top:1px solid #e6e6e6;display:flex;justify-content:space-around;align-items:center;padding:0 6px}
.member-links svg{width:13px;height:13px}
.member.is-active{background:var(--teal);border-color:var(--teal)}
.member.is-active .member-name,.member.is-active .member-role,.member.is-active .member-bio{color:var(--white)}
.member.is-active .member-links{border-top-color:var(--teal-dark)}
.tone-a{background:linear-gradient(135deg,#cfd6dd,#a18574 55%,#e8ecef)}
.tone-b{background:linear-gradient(135deg,#8a7a66,#c79c7a 50%,#f0e8de)}
.tone-c{background:linear-gradient(135deg,#d9d4cc,#3a3330 55%,#b3302a)}
.tone-d{background:linear-gradient(135deg,#2f3a24,#6e8a3a 45%,#c9a08a)}
.site-footer{position:absolute;left:0;top:931px;width:676px;height:201px;background:var(--footer)}
.footer-about{width:320px;margin:26px auto 0;text-align:center;font-size:7.6px;line-height:9.6px;color:var(--white)}
.contacts{position:absolute;left:174px;top:108px;display:flex;gap:34px;font-size:6.3px;line-height:8px;color:var(--white)}
.contact{display:flex;align-items:center;gap:9px}
.footer-base{position:absolute;left:0;top:1132px;width:676px;height:68px;background:var(--footer-deep)}
.socials{position:absolute;left:290px;top:13px;display:flex;gap:7px}
.socials span{width:18px;height:18px;border:1px solid #c6c6c6;border-radius:50%}
.base-rule{position:absolute;left:84px;top:38px;width:508px;height:1px;background:#b3b3b3}
.copyright{position:absolute;left:0;top:48px;width:676px;text-align:center;font-size:5.4px;line-height:6.4px;color:var(--white)}
</style>
</head>
<body>
<header class="site-header">
  <div class="brand"><span class="brand-dot"></span><span class="brand-name">QONDIMEX</span></div>
</header>
<nav class="main-nav">
  <a href="#">Servers</a><a href="#">Workstations</a><a href="#">Components</a><a href="#">Virtual Reality</a><a href="#">Drones</a><a href="#">About us</a><a href="#">Blog</a><a href="#">Resources</a><a href="#">Contact Us</a>
</nav>
<div class="search">Search</div>
<div class="basket"><svg viewBox="0 0 16 16" width="16" height="16"><path d="M4.5 6.5h7l-1 4.5h-5z" fill="none" stroke="#fff" stroke-width="1"/></svg></div>
<div class="crumbs"><svg viewBox="0 0 8 8" width="6" height="6"><path d="M4 0.5 0.5 4h1v3.5h2v-2h1v2h2V4h1z" fill="#fff"/></svg><span>—</span><span>Meet our team</span></div>

<section class="intro">
  <h1>We're an experienced and specialist team<br>committed to deliver better solutions</h1>
  <p>We are a team committed to give you a profesional service and support tooobtain major brand hardware at discounted rates and faster response times. Our on-site testing facility fully examines all equipment to ensure that all hardware shipped and received succeeds industry standards for quality control.</p>
</section>

<main class="team">
  <!-- card template repeated per member -->
  <article class="member is-active">
    <div class="member-photo tone-a" role="img" aria-label="Portrait photo of Owen Hartley"></div>
    <div class="member-body"><h2 class="member-name">Owen Hartley</h2><div class="member-role">Founder &amp; CEO</div>
      <p class="member-bio">Lorem ipsum dolor sit amet, constetur adipiscing elit, sed do eiusmod tempor incididunt ut labore et dolore magna aliqua. Ut enim ad minim veniam, quis nostrud exercitation.</p>
      <p class="member-bio">Duis aute irure dolor in reprehenderit in voluptate velit esse cillum dolore eu fugiat nulla pariatur. Excepteur sint occaecat cupidatat non proident, sunt in culpa qui officia deserunt mollit anim id est laborum.</p></div>
    <div class="member-links">
      <svg viewBox="0 0 13 13"><circle cx="6.5" cy="6.5" r="6.5" fill="#fff"/></svg>
      <svg viewBox="0 0 13 13"><circle cx="6.5" cy="6.5" r="6.5" fill="#fff"/></svg>
      <svg viewBox="0 0 13 13"><circle cx="6.5" cy="6.5" r="6.5" fill="#fff"/><rect x="3.5" y="4.5" width="6" height="4" fill="#4dbcb4"/><path d="M3.5 4.5 6.5 7 9.5 4.5" fill="none" stroke="#fff" stroke-width=".6"/></svg>
      <svg viewBox="0 0 13 13"><circle cx="6.5" cy="6.5" r="6.5" fill="#fff"/><path d="M4.3 3.8c.4-.4.9-.3 1.1.1l.5 1c.1.3 0 .6-.3.8l-.3.2c.4.9 1 1.5 1.9 1.9l.2-.3c.2-.3.5-.4.8-.3l1 .5c.4.2.5.7.1 1.1-1.8 1.5-6.5-3.2-5-5z" fill="#4dbcb4"/></svg>
      <svg viewBox="0 0 13 13"><circle cx="6.5" cy="6.5" r="6.5" fill="#fff"/></svg>
    </div>
  </article>
  <article class="member">
    <div class="member-photo tone-b" role="img" aria-label="Portrait photo of Felix Brandt"></div>
    <div class="member-body"><h2 class="member-name">Felix Brandt</h2><div class="member-role">Founder &amp; CEO</div>
      <p class="member-bio">Lorem ipsum dolor sit amet, constetur adipiscing elit, sed do eiusmod tempor incididunt ut labore et dolore magna aliqua. Ut enim ad minim veniam, quis nostrud exercitation.</p>
      <p class="member-bio">Duis aute irure dolor in reprehenderit in voluptate velit esse cillum dolore eu fugiat nulla pariatur. Excepteur sint occaecat cupidatat non proident, sunt in culpa qui officia deserunt mollit anim id est laborum.</p></div>
    <div class="member-links">
      <svg viewBox="0 0 13 13"><circle cx="6.5" cy="6.5" r="6" fill="#e3f3f2"/></svg>
      <svg viewBox="0 0 13 13"><circle cx="6.5" cy="6.5" r="6" fill="#e3f3f2"/></svg>
      <svg viewBox="0 0 13 13"><circle cx="6.5" cy="6.5" r="6" fill="#e3f3f2"/><rect x="3.5" y="4.5" width="6" height="4" fill="#4dbcb4"/><path d="M3.5 4.5 6.5 7 9.5 4.5" fill="none" stroke="#e3f3f2" stroke-width=".6"/></svg>
      <svg viewBox="0 0 13 13"><circle cx="6.5" cy="6.5" r="6" fill="#e3f3f2"/><path d="M4.3 3.8c.4-.4.9-.3 1.1.1l.5 1c.1.3 0 .6-.3.8l-.3.2c.4.9 1 1.5 1.9 1.9l.2-.3c.2-.3.5-.4.8-.3l1 .5c.4.2.5.7.1 1.1-1.8 1.5-6.5-3.2-5-5z" fill="#4dbcb4"/></svg>
      <svg viewBox="0 0 13 13"><circle cx="6.5" cy="6.5" r="6" fill="#e3f3f2"/></svg>
    </div>
  </article>
  <article class="member">
    <div class="member-photo tone-c" role="img" aria-label="Portrait photo of Mira Castell"></div>
    <div class="member-body"><h2 class="member-name">Mira Castell</h2><div class="member-role">Founder &amp; CEO</div>
      <p class="member-bio">Lorem ipsum dolor sit amet, constetur adipiscing elit, sed do eiusmod tempor incididunt ut labore et dolore magna aliqua. Ut enim ad minim veniam, quis nostrud exercitation.</p>
      <p class="member-bio">Duis aute irure dolor in reprehenderit in voluptate velit esse cillum dolore eu fugiat nulla pariatur. Excepteur sint occaecat cupidatat non proident, sunt in culpa qui officia deserunt mollit anim id est laborum.</p></div>
    <div class="member-links">
      <svg viewBox="0 0 13 13"><circle cx="6.5" cy="6.5" r="6" fill="#e3f3f2"/></svg>
      <svg viewBox="0 0 13 13"><circle cx="6.5" cy="6.5" r="6" fill="#e3f3f2"/></svg>
      <svg viewBox="0 0 13 13"><circle cx="6.5" cy="6.5" r="6" fill="#e3f3f2"/><rect x="3.5" y="4.5" width="6" height="4" fill="#4dbcb4"/><path d="M3.5 4.5 6.5 7 9.5 4.5" fill="none" stroke="#e3f3f2" stroke-width=".6"/></svg>
      <svg viewBox="0 0 13 13"><circle cx="6.5" cy="6.5" r="6" fill="#e3f3f2"/><path d="M4.3 3.8c.4-.4.9-.3 1.1.1l.5 1c.1.3 0 .6-.3.8l-.3.2c.4.9 1 1.5 1.9 1.9l.2-.3c.2-.3.5-.4.8-.3l1 .5c.4.2.5.7.1 1.1-1.8 1.5-6.5-3.2-5-5z" fill="#4dbcb4"/></svg>
      <svg viewBox="0 0 13 13"><circle cx="6.5" cy="6.5" r="6" fill="#e3f3f2"/></svg>
    </div>
  </article>
  <article class="member">
    <div class="member-photo tone-d" role="img" aria-label="Portrait photo of Lena Holloway"></div>
    <div class="member-body"><h2 class="member-name">Lena Holloway</h2><div class="member-role">Founder &amp; CEO</div>
      <p class="member-bio">Lorem ipsum dolor sit amet, constetur adipiscing elit, sed do eiusmod tempor incididunt ut labore et dolore magna aliqua. Ut enim ad minim veniam, quis nostrud exercitation.</p>
      <p class="member-bio">Duis aute irure dolor in reprehenderit in voluptate velit esse cillum dolore eu fugiat nulla pariatur. Excepteur sint occaecat cupidatat non proident, sunt in culpa qui officia deserunt mollit anim id est laborum.</p></div>
    <div class="member-links">
      <svg viewBox="0 0 13 13"><circle cx="6.5" cy="6.5" r="6" fill="#e3f3f2"/></svg>
      <svg viewBox="0 0 13 13"><circle cx="6.5" cy="6.5" r="6" fill="#e3f3f2"/></svg>
      <svg viewBox="0 0 13 13"><circle cx="6.5" cy="6.5" r="6" fill="#e3f3f2"/><rect x="3.5" y="4.5" width="6" height="4" fill="#4dbcb4"/><path d="M3.5 4.5 6.5 7 9.5 4.5" fill="none" stroke="#e3f3f2" stroke-width=".6"/></svg>
      <svg viewBox="0 0 13 13"><circle cx="6.5" cy="6.5" r="6" fill="#e3f3f2"/><path d="M4.3 3.8c.4-.4.9-.3 1.1.1l.5 1c.1.3 0 .6-.3.8l-.3.2c.4.9 1 1.5 1.9 1.9l.2-.3c.2-.3.5-.4.8-.3l1 .5c.4.2.5.7.1 1.1-1.8 1.5-6.5-3.2-5-5z" fill="#4dbcb4"/></svg>
      <svg viewBox="0 0 13 13"><circle cx="6.5" cy="6.5" r="6" fill="#e3f3f2"/></svg>
    </div>
  </article>
  <article class="member">
    <div class="member-photo tone-a" role="img" aria-label="Portrait photo of Tess Whitford"></div>
    <div class="member-body"><h2 class="member-name">Tess Whitford</h2><div class="member-role">Founder &amp; CEO</div>
      <p class="member-bio">Lorem ipsum dolor sit amet, constetur adipiscing elit, sed do eiusmod tempor incididunt ut labore et dolore magna aliqua. Ut enim ad minim veniam, quis nostrud exercitation.</p>
      <p class="member-bio">Duis aute irure dolor in reprehenderit in voluptate velit esse cillum dolore eu fugiat nulla pariatur. Excepteur sint occaecat cupidatat non proident, sunt in culpa qui officia deserunt mollit anim id est laborum.</p></div>
    <div class="member-links">
      <svg viewBox="0 0 13 13"><circle cx="6.5" cy="6.5" r="6" fill="#e3f3f2"/></svg>
      <svg viewBox="0 0 13 13"><circle cx="6.5" cy="6.5" r="6" fill="#e3f3f2"/></svg>
      <svg viewBox="0 0 13 13"><circle cx="6.5" cy="6.5" r="6" fill="#e3f3f2"/><rect x="3.5" y="4.5" width="6" height="4" fill="#4dbcb4"/><path d="M3.5 4.5 6.5 7 9.5 4.5" fill="none" stroke="#e3f3f2" stroke-width=".6"/></svg>
      <svg viewBox="0 0 13 13"><circle cx="6.5" cy="6.5" r="6" fill="#e3f3f2"/><path d="M4.3 3.8c.4-.4.9-.3 1.1.1l.5 1c.1.3 0 .6-.3.8l-.3.2c.4.9 1 1.5 1.9 1.9l.2-.3c.2-.3.5-.4.8-.3l1 .5c.4.2.5.7.1 1.1-1.8 1.5-6.5-3.2-5-5z" fill="#4dbcb4"/></svg>
      <svg viewBox="0 0 13 13"><circle cx="6.5" cy="6.5" r="6" fill="#e3f3f2"/></svg>
    </div>
  </article>
  <article class="member">
    <div class="member-photo tone-b" role="img" aria-label="Portrait photo of Rowan Pike"></div>
    <div class="member-body"><h2 class="member-name">Rowan Pike</h2><div class="member-role">Founder &amp; CEO</div>
      <p class="member-bio">Lorem ipsum dolor sit amet, constetur adipiscing elit, sed do eiusmod tempor incididunt ut labore et dolore magna aliqua. Ut enim ad minim veniam, quis nostrud exercitation.</p>
      <p class="member-bio">Duis aute irure dolor in reprehenderit in voluptate velit esse cillum dolore eu fugiat nulla pariatur. Excepteur sint occaecat cupidatat non proident, sunt in culpa qui officia deserunt mollit anim id est laborum.</p></div>
    <div class="member-links">
      <svg viewBox="0 0 13 13"><circle cx="6.5" cy="6.5" r="6" fill="#e3f3f2"/></svg>
      <svg viewBox="0 0 13 13"><circle cx="6.5" cy="6.5" r="6" fill="#e3f3f2"/></svg>
      <svg viewBox="0 0 13 13"><circle cx="6.5" cy="6.5" r="6" fill="#e3f3f2"/><rect x="3.5" y="4.5" width="6" height="4" fill="#4dbcb4"/><path d="M3.5 4.5 6.5 7 9.5 4.5" fill="none" stroke="#e3f3f2" stroke-width=".6"/></svg>
      <svg viewBox="0 0 13 13"><circle cx="6.5" cy="6.5" r="6" fill="#e3f3f2"/><path d="M4.3 3.8c.4-.4.9-.3 1.1.1l.5 1c.1.3 0 .6-.3.8l-.3.2c.4.9 1 1.5 1.9 1.9l.2-.3c.2-.3.5-.4.8-.3l1 .5c.4.2.5.7.1 1.1-1.8 1.5-6.5-3.2-5-5z" fill="#4dbcb4"/></svg>
      <svg viewBox="0 0 13 13"><circle cx="6.5" cy="6.5" r="6" fill="#e3f3f2"/></svg>
    </div>
  </article>
  <article class="member">
    <div class="member-photo tone-c" role="img" aria-label="Portrait photo of Ines Calder"></div>
    <div class="member-body"><h2 class="member-name">Ines Calder</h2><div class="member-role">Founder &amp; CEO</div>
      <p class="member-bio">Lorem ipsum dolor sit amet, constetur adipiscing elit, sed do eiusmod tempor incididunt ut labore et dolore magna aliqua. Ut enim ad minim veniam, quis nostrud exercitation.</p>
      <p class="member-bio">Duis aute irure dolor in reprehenderit in voluptate velit esse cillum dolore eu fugiat nulla pariatur. Excepteur sint occaecat cupidatat non proident, sunt in culpa qui officia deserunt mollit anim id est laborum.</p></div>
    <div class="member-links">
      <svg viewBox="0 0 13 13"><circle cx="6.5" cy="6.5" r="6" fill="#e3f3f2"/></svg>
      <svg viewBox="0 0 13 13"><circle cx="6.5" cy="6.5" r="6" fill="#e3f3f2"/></svg>
      <svg viewBox="0 0 13 13"><circle cx="6.5" cy="6.5" r="6" fill="#e3f3f2"/><rect x="3.5" y="4.5" width="6" height="4" fill="#4dbcb4"/><path d="M3.5 4.5 6.5 7 9.5 4.5" fill="none" stroke="#e3f3f2" stroke-width=".6"/></svg>
      <svg viewBox="0 0 13 13"><circle cx="6.5" cy="6.5" r="6" fill="#e3f3f2"/><path d="M4.3 3.8c.4-.4.9-.3 1.1.1l.5 1c.1.3 0 .6-.3.8l-.3.2c.4.9 1 1.5 1.9 1.9l.2-.3c.2-.3.5-.4.8-.3l1 .5c.4.2.5.7.1 1.1-1.8 1.5-6.5-3.2-5-5z" fill="#4dbcb4"/></svg>
      <svg viewBox="0 0 13 13"><circle cx="6.5" cy="6.5" r="6" fill="#e3f3f2"/></svg>
    </div>
  </article>
  <article class="member">
    <div class="member-photo tone-d" role="img" aria-label="Portrait photo of Nora Lindqvist"></div>
    <div class="member-body"><h2 class="member-name">Nora Lindqvist</h2><div class="member-role">Founder &amp; CEO</div>
      <p class="member-bio">Lorem ipsum dolor sit amet, constetur adipiscing elit, sed do eiusmod tempor incididunt ut labore et dolore magna aliqua. Ut enim ad minim veniam, quis nostrud exercitation.</p>
      <p class="member-bio">Duis aute irure dolor in reprehenderit in voluptate velit esse cillum dolore eu fugiat nulla pariatur. Excepteur sint occaecat cupidatat non proident, sunt in culpa qui officia deserunt mollit anim id est laborum.</p></div>
    <div class="member-links">
      <svg viewBox="0 0 13 13"><circle cx="6.5" cy="6.5" r="6" fill="#e3f3f2"/></svg>
      <svg viewBox="0 0 13 13"><circle cx="6.5" cy="6.5" r="6" fill="#e3f3f2"/></svg>
      <svg viewBox="0 0 13 13"><circle cx="6.5" cy="6.5" r="6" fill="#e3f3f2"/><rect x="3.5" y="4.5" width="6" height="4" fill="#4dbcb4"/><path d="M3.5 4.5 6.5 7 9.5 4.5" fill="none" stroke="#e3f3f2" stroke-width=".6"/></svg>
      <svg viewBox="0 0 13 13"><circle cx="6.5" cy="6.5" r="6" fill="#e3f3f2"/><path d="M4.3 3.8c.4-.4.9-.3 1.1.1l.5 1c.1.3 0 .6-.3.8l-.3.2c.4.9 1 1.5 1.9 1.9l.2-.3c.2-.3.5-.4.8-.3l1 .5c.4.2.5.7.1 1.1-1.8 1.5-6.5-3.2-5-5z" fill="#4dbcb4"/></svg>
      <svg viewBox="0 0 13 13"><circle cx="6.5" cy="6.5" r="6" fill="#e3f3f2"/></svg>
    </div>
  </article>
  <article class="member">
    <div class="member-photo tone-a" role="img" aria-label="Portrait photo of Tomas Ferrer"></div>
    <div class="member-body"><h2 class="member-name">Tomas Ferrer</h2><div class="member-role">Founder &amp; CEO</div>
      <p class="member-bio">Lorem ipsum dolor sit amet, constetur adipiscing elit, sed do eiusmod tempor incididunt ut labore et dolore magna aliqua. Ut enim ad minim veniam, quis nostrud exercitation.</p>
      <p class="member-bio">Duis aute irure dolor in reprehenderit in voluptate velit esse cillum dolore eu fugiat nulla pariatur. Excepteur sint occaecat cupidatat non proident, sunt in culpa qui officia deserunt mollit anim id est laborum.</p></div>
    <div class="member-links">
      <svg viewBox="0 0 13 13"><circle cx="6.5" cy="6.5" r="6" fill="#e3f3f2"/></svg>
      <svg viewBox="0 0 13 13"><circle cx="6.5" cy="6.5" r="6" fill="#e3f3f2"/></svg>
      <svg viewBox="0 0 13 13"><circle cx="6.5" cy="6.5" r="6" fill="#e3f3f2"/><rect x="3.5" y="4.5" width="6" height="4" fill="#4dbcb4"/><path d="M3.5 4.5 6.5 7 9.5 4.5" fill="none" stroke="#e3f3f2" stroke-width=".6"/></svg>
      <svg viewBox="0 0 13 13"><circle cx="6.5" cy="6.5" r="6" fill="#e3f3f2"/><path d="M4.3 3.8c.4-.4.9-.3 1.1.1l.5 1c.1.3 0 .6-.3.8l-.3.2c.4.9 1 1.5 1.9 1.9l.2-.3c.2-.3.5-.4.8-.3l1 .5c.4.2.5.7.1 1.1-1.8 1.5-6.5-3.2-5-5z" fill="#4dbcb4"/></svg>
      <svg viewBox="0 0 13 13"><circle cx="6.5" cy="6.5" r="6" fill="#e3f3f2"/></svg>
    </div>
  </article>
  <article class="member">
    <div class="member-photo tone-b" role="img" aria-label="Portrait photo of Vera Dunmore"></div>
    <div class="member-body"><h2 class="member-name">Vera Dunmore</h2><div class="member-role">Founder &amp; CEO</div>
      <p class="member-bio">Lorem ipsum dolor sit amet, constetur adipiscing elit, sed do eiusmod tempor incididunt ut labore et dolore magna aliqua. Ut enim ad minim veniam, quis nostrud exercitation.</p>
      <p class="member-bio">Duis aute irure dolor in reprehenderit in voluptate velit esse cillum dolore eu fugiat nulla pariatur. Excepteur sint occaecat cupidatat non proident, sunt in culpa qui officia deserunt mollit anim id est laborum.</p></div>
    <div class="member-links">
      <svg viewBox="0 0 13 13"><circle cx="6.5" cy="6.5" r="6" fill="#e3f3f2"/></svg>
      <svg viewBox="0 0 13 13"><circle cx="6.5" cy="6.5" r="6" fill="#e3f3f2"/></svg>
      <svg viewBox="0 0 13 13"><circle cx="6.5" cy="6.5" r="6" fill="#e3f3f2"/><rect x="3.5" y="4.5" width="6" height="4" fill="#4dbcb4"/><path d="M3.5 4.5 6.5 7 9.5 4.5" fill="none" stroke="#e3f3f2" stroke-width=".6"/></svg>
      <svg viewBox="0 0 13 13"><circle cx="6.5" cy="6.5" r="6" fill="#e3f3f2"/><path d="M4.3 3.8c.4-.4.9-.3 1.1.1l.5 1c.1.3 0 .6-.3.8l-.3.2c.4.9 1 1.5 1.9 1.9l.2-.3c.2-.3.5-.4.8-.3l1 .5c.4.2.5.7.1 1.1-1.8 1.5-6.5-3.2-5-5z" fill="#4dbcb4"/></svg>
      <svg viewBox="0 0 13 13"><circle cx="6.5" cy="6.5" r="6" fill="#e3f3f2"/></svg>
    </div>
  </article>
  <article class="member">
    <div class="member-photo tone-c" role="img" aria-label="Portrait photo of Aline Marchand"></div>
    <div class="member-body"><h2 class="member-name">Aline Marchand</h2><div class="member-role">Founder &amp; CEO</div>
      <p class="member-bio">Lorem ipsum dolor sit amet, constetur adipiscing elit, sed do eiusmod tempor incididunt ut labore et dolore magna aliqua. Ut enim ad minim veniam, quis nostrud exercitation.</p>
      <p class="member-bio">Duis aute irure dolor in reprehenderit in voluptate velit esse cillum dolore eu fugiat nulla pariatur. Excepteur sint occaecat cupidatat non proident, sunt in culpa qui officia deserunt mollit anim id est laborum.</p></div>
    <div class="member-links">
      <svg viewBox="0 0 13 13"><circle cx="6.5" cy="6.5" r="6" fill="#e3f3f2"/></svg>
      <svg viewBox="0 0 13 13"><circle cx="6.5" cy="6.5" r="6" fill="#e3f3f2"/></svg>
      <svg viewBox="0 0 13 13"><circle cx="6.5" cy="6.5" r="6" fill="#e3f3f2"/><rect x="3.5" y="4.5" width="6" height="4" fill="#4dbcb4"/><path d="M3.5 4.5 6.5 7 9.5 4.5" fill="none" stroke="#e3f3f2" stroke-width=".6"/></svg>
      <svg viewBox="0 0 13 13"><circle cx="6.5" cy="6.5" r="6" fill="#e3f3f2"/><path d="M4.3 3.8c.4-.4.9-.3 1.1.1l.5 1c.1.3 0 .6-.3.8l-.3.2c.4.9 1 1.5 1.9 1.9l.2-.3c.2-.3.5-.4.8-.3l1 .5c.4.2.5.7.1 1.1-1.8 1.5-6.5-3.2-5-5z" fill="#4dbcb4"/></svg>
      <svg viewBox="0 0 13 13"><circle cx="6.5" cy="6.5" r="6" fill="#e3f3f2"/></svg>
    </div>
  </article>
  <article class="member">
    <div class="member-photo tone-d" role="img" aria-label="Portrait photo of Mira Castell"></div>
    <div class="member-body"><h2 class="member-name">Mira Castell</h2><div class="member-role">Founder &amp; CEO</div>
      <p class="member-bio">Lorem ipsum dolor sit amet, constetur adipiscing elit, sed do eiusmod tempor incididunt ut labore et dolore magna aliqua. Ut enim ad minim veniam, quis nostrud exercitation.</p>
      <p class="member-bio">Duis aute irure dolor in reprehenderit in voluptate velit esse cillum dolore eu fugiat nulla pariatur. Excepteur sint occaecat cupidatat non proident, sunt in culpa qui officia deserunt mollit anim id est laborum.</p></div>
    <div class="member-links">
      <svg viewBox="0 0 13 13"><circle cx="6.5" cy="6.5" r="6" fill="#e3f3f2"/></svg>
      <svg viewBox="0 0 13 13"><circle cx="6.5" cy="6.5" r="6" fill="#e3f3f2"/></svg>
      <svg viewBox="0 0 13 13"><circle cx="6.5" cy="6.5" r="6" fill="#e3f3f2"/><rect x="3.5" y="4.5" width="6" height="4" fill="#4dbcb4"/><path d="M3.5 4.5 6.5 7 9.5 4.5" fill="none" stroke="#e3f3f2" stroke-width=".6"/></svg>
      <svg viewBox="0 0 13 13"><circle cx="6.5" cy="6.5" r="6" fill="#e3f3f2"/><path d="M4.3 3.8c.4-.4.9-.3 1.1.1l.5 1c.1.3 0 .6-.3.8l-.3.2c.4.9 1 1.5 1.9 1.9l.2-.3c.2-.3.5-.4.8-.3l1 .5c.4.2.5.7.1 1.1-1.8 1.5-6.5-3.2-5-5z" fill="#4dbcb4"/></svg>
      <svg viewBox="0 0 13 13"><circle cx="6.5" cy="6.5" r="6" fill="#e3f3f2"/></svg>
    </div>
  </article>
</main>

<footer class="site-footer">
  <p class="footer-about">Based in Maple Grove California, Qondimex offers custom servers, storage, and workstations for local businesses in Los Angeles, Beverly Hills, Thousand Oaks, Ventura, Orange County, Santa Barbara, Oxnard, Irvine, Anaheim, and San Diego. Qondimex also offers such products to clients throughout the United States and Worldwide.</p>
  <div class="contacts">
    <div class="contact"><svg viewBox="0 0 8 12" width="7" height="11"><path d="M4 0a4 4 0 0 0-4 4c0 3 4 8 4 8s4-5 4-8a4 4 0 0 0-4-4zm0 5.5a1.5 1.5 0 1 1 0-3 1.5 1.5 0 0 1 0 3z" fill="#fff"/></svg><span>4820 Larkfield Ave.<br>Maple Grove, CA 91388</span></div>
    <div class="contact"><svg viewBox="0 0 12 12" width="10" height="10"><path d="M2 1c.7-.7 1.5-.5 1.9.2l.9 1.7c.2.5 0 1-.5 1.3l-.5.4c.7 1.5 1.7 2.5 3.2 3.2l.4-.5c.3-.5.8-.7 1.3-.5l1.7.9c.7.4.9 1.2.2 1.9C7.6 12.3-.7 4 2 1z" fill="#fff"/></svg><span>555-204-7718</span></div>
    <div class="contact" style="margin-left:14px"><svg viewBox="0 0 14 10" width="13" height="9"><rect width="14" height="10" fill="#fff"/><path d="M0 0 7 5.5 14 0" fill="none" stroke="#a4a4a4" stroke-width="1"/></svg><span>sales@qondimex.com</span></div>
  </div>
</footer>
<div class="footer-base">
  <div class="socials"><span></span><span></span><span></span><span></span></div>
  <div class="base-rule"></div>
  <p class="copyright">Qondimex, LLC.<br>Copyright © 2017</p>
</div>
</body>
</html>
```